Young and modern Electrical company working in the commercial arena.

Wanting a business card design thats modern and will last. Maybe Minimalist? Happy to look at changing my logo

Target Market(s)

Builders, Project Managers

Industry/Entity Type

Electrical

Contact Information for Business Card

Name
Address
Phone number
Job title

Logo Text

our name or just the logo i'm open to ideas

Font styles to use
Sans Serif

Requirements
Nice to have
• would like to keep the purple in our current logo. it's kinda unique to our market
Should not have
• Don't want it to be to busy. simple is best i think

```html
<!DOCTYPE html>
<html lang="en">
<head>
<meta charset="utf-8">
<title>Hartwell Electrical – Business Card</title>
<link rel="stylesheet" href="https://fonts.googleapis.com/css2?family=Jost:wght@400;600&family=Open+Sans:wght@400;600&display=swap">
<style>
  :root {
    --purple: #522b80;
    --card: #f2f2f2;
    --ink: #111111;
    --white: #ffffff;
    --stage: #e4e2e6;
  }
  * { margin: 0; padding: 0; box-sizing: border-box; }
  html, body {
    width: 1200px;
    height: 1200px;
    overflow: hidden;
    background: var(--stage);
  }
  .canvas {
    position: relative;
    width: 1200px;
    height: 1200px;
  }
  .card {
    position: absolute;
    top: 250px;
    width: 400px;
    height: 700px;
    background: var(--card);
    overflow: hidden;
    box-shadow: 0 6px 18px rgba(0, 0, 0, 0.18);
  }
  .card--front { left: 164px; }
  .card--back { left: 636px; }

  /* Front */
  .brand {
    position: absolute;
    top: 160px;
    left: 72px;
    display: flex;
    align-items: center;
    gap: 18px;
  }
  .brand__mark {
    width: 86px;
    height: 86px;
    border: 5px solid var(--purple);
    border-radius: 50%;
    flex: none;
  }
  .brand__name {
    font-family: "Jost", sans-serif;
    font-weight: 400;
    font-size: 27px;
    line-height: 1.15;
    letter-spacing: 1px;
    color: var(--ink);
  }
  .front-band {
    position: absolute;
    left: 0;
    bottom: 0;
    width: 100%;
    height: 19px;
    background: var(--purple);
    border-radius: 8px 8px 0 0;
  }

  /* Back */
  .identity {
    position: absolute;
    top: 0;
    left: 0;
    width: 100%;
    height: 448px;
    background: var(--purple);
    color: var(--white);
  }
  .identity__name {
    position: absolute;
    top: 286px;
    left: 42px;
    font-family: "Jost", sans-serif;
    font-size: 41px;
    font-weight: 400;
    line-height: 1;
    letter-spacing: 0.5px;
  }
  .identity__name strong { font-weight: 600; }
  .identity__title {
    position: absolute;
    top: 334px;
    left: 50px;
    font-family: "Open Sans", sans-serif;
    font-size: 20px;
    font-weight: 400;
  }
  .contact {
    position: absolute;
    left: 40px;
    top: 555px;
    list-style: none;
    font-family: "Open Sans", sans-serif;
    font-weight: 600;
    font-size: 18.5px;
    line-height: 25px;
    color: var(--purple);
  }
  .contact__item {
    display: flex;
    align-items: flex-start;
    gap: 12px;
    margin-bottom: 21px;
  }
  .contact__icon {
    width: 20px;
    height: 24px;
    flex: none;
    margin-top: 1px;
  }
</style>
</head>
<body>
<main class="canvas">
  <section class="card card--front">
    <div class="brand">
      <span class="brand__mark"></span>
      <div class="brand__name">Hartwell<br>Electrical</div>
    </div>
    <div class="front-band"></div>
  </section>

  <section class="card card--back">
    <div class="identity">
      <h1 class="identity__name"><strong>YOUR</strong> NAME</h1>
      <p class="identity__title">job title</p>
    </div>
    <ul class="contact">
      <li class="contact__item">
        <svg class="contact__icon" viewBox="0 0 20 24" aria-hidden="true">
          <path d="M10 2a7 7 0 0 0-7 7c0 5 7 13 7 13s7-8 7-13a7 7 0 0 0-7-7z" fill="none" stroke="#522b80" stroke-width="2.4"/>
          <circle cx="10" cy="9" r="2.6" fill="none" stroke="#522b80" stroke-width="2"/>
        </svg>
        <span>123 loremipsum, lorem<br>loremipsum 78910</span>
      </li>
      <li class="contact__item">
        <svg class="contact__icon" viewBox="0 0 24 24" aria-hidden="true">
          <path d="M6.6 10.8a15 15 0 0 0 6.6 6.6l2.2-2.2a1 1 0 0 1 1-.25 11.4 11.4 0 0 0 3.6.57 1 1 0 0 1 1 1V20a1 1 0 0 1-1 1A17 17 0 0 1 3 4a1 1 0 0 1 1-1h3.5a1 1 0 0 1 1 1c0 1.25.2 2.45.57 3.57a1 1 0 0 1-.25 1z" fill="#522b80"/>
        </svg>
        <span>+11 (0) 222 333 44 55</span>
      </li>
    </ul>
  </section>
</main>
</body>
</html>
```